Business Card Design For A Renovation Contractor Company

We need a business card for a new company based in Singapore, our company name is "KT Planora". We are a renovation contractor that builds designs into reality. We build more of F&B restaurants, retail stores and commercial offices. We work very closely with designers. The final design should communicate to our client that we are a company that you can trust, that will plan and complete your project without giving you a headache. I like my client to remember my company as "KT". The beauty of SIMPLE is important.

Industry/Entity Type

Contractor

Requirements
Nice to have
• Black or Red base

```html
<!DOCTYPE html>
<html lang="en">
<head>
<meta charset="utf-8">
<title>KT Planora – Business Card</title>
<link rel="stylesheet" href="https://fonts.googleapis.com/css2?family=Open+Sans:wght@400;600;700&display=swap">
<style>
  :root {
    --bg: #e9ebee;
    --card: #ffffff;
    --ink: #1a1a1a;
    --red: #e3161b;
    --black: #0c0c0c;
    --rule: #d6d6d6;
    --muted: #3a3a3a;
  }
  * { box-sizing: border-box; margin: 0; padding: 0; }
  html, body {
    width: 1200px; height: 987px; overflow: hidden;
    background: var(--bg);
    font-family: "Open Sans", Arial, sans-serif;
    color: var(--ink);
  }
  .canvas { position: relative; width: 1200px; height: 987px; }
  .card {
    position: absolute; left: 240px;
    width: 720px; height: 420px;
    background: var(--card);
    border-radius: 26px;
    overflow: hidden;
    box-shadow: 0 6px 18px rgba(0,0,0,.12);
  }
  .card--back { top: 50px; }
  .card--front { top: 517px; }

  .brand { position: absolute; display: flex; flex-direction: column; }
  .brand__row { display: flex; align-items: center; gap: 14px; }
  .brand__dot {
    width: 30px; height: 30px; border-radius: 50%;
    background: var(--red);
  }
  .brand__name {
    font-weight: 400; font-size: 54px; line-height: 1;
    color: var(--red); letter-spacing: -0.5px;
  }
  .brand__tagline {
    margin-top: 6px; padding-top: 4px;
    border-top: 1.5px solid var(--muted);
    font-size: 19px; color: var(--muted); letter-spacing: 0.3px;
    white-space: nowrap;
  }

  .card--back .brand { left: 50%; top: 130px; transform: translateX(-50%); }
  .back__web {
    position: absolute; left: 0; right: 0; top: 290px;
    text-align: center; font-size: 22px; letter-spacing: 5px; color: var(--muted);
  }
  .back__web .accent { color: var(--red); font-weight: 600; }

  .card--front .brand { left: 60px; top: 64px; }
  .card--front .brand__name { font-size: 48px; }
  .card--front .brand__tagline { font-size: 17px; }

  .wave { position: absolute; inset: 0; }
  .front__web {
    position: absolute; left: 34px; top: 268px;
    transform: rotate(24deg); transform-origin: left top;
    color: #fff; font-size: 20px; letter-spacing: 4px;
    white-space: nowrap;
  }

  .divider {
    position: absolute; left: 440px; top: 40px; width: 1px; height: 220px;
    background: linear-gradient(var(--rule), rgba(214,214,214,0));
  }
  .contact { position: absolute; left: 468px; top: 44px; }
  .contact__name { font-weight: 700; font-size: 24px; line-height: 1.1; }
  .contact__title { color: var(--red); font-size: 18px; margin-bottom: 12px; }
  .contact__line {
    display: flex; align-items: center; gap: 10px;
    font-size: 19px; line-height: 1.5; color: var(--muted);
  }
  .contact__line svg { width: 16px; height: 16px; flex: none; }
  .contact__address { margin-top: 6px; font-size: 19px; line-height: 1.35; color: var(--muted); }
</style>
</head>
<body>
<main class="canvas">

  <section class="card card--back" aria-label="Card back">
    <div class="brand">
      <div class="brand__row">
        <span class="brand__dot"></span>
        <span class="brand__name">KT Planora</span>
      </div>
      <span class="brand__tagline">planning every build with care</span>
    </div>
    <p class="back__web">www.<span class="accent">ktplanora</span>.com</p>
  </section>

  <section class="card card--front" aria-label="Card front">
    <svg class="wave" viewBox="0 0 720 420" preserveAspectRatio="none" aria-hidden="true">
      <path d="M0,178 C190,188 320,320 690,420 L610,420 C300,336 180,214 0,206 Z" fill="var(--red)"/>
      <path d="M0,214 C180,222 300,340 600,420 L0,420 Z" fill="var(--black)"/>
      <path d="M430,300 C520,360 600,392 720,404 L720,412 C600,402 510,372 430,306 Z" fill="var(--red)"/>
    </svg>
    <p class="front__web">www.ktplanora.com</p>

    <div class="brand">
      <div class="brand__row">
        <span class="brand__dot"></span>
        <span class="brand__name">KT Planora</span>
      </div>
      <span class="brand__tagline">planning every build with care</span>
    </div>

    <div class="divider"></div>

    <div class="contact">
      <p class="contact__name">Your Name</p>
      <p class="contact__title">Title</p>
      <p class="contact__line">
        <svg viewBox="0 0 16 16" aria-hidden="true"><path d="M4 1l3 3-2 2c1 2 3 4 5 5l2-2 3 3-2 3C7 15 1 9 1 3z" fill="var(--red)"/></svg>
        123-456-0789
      </p>
      <p class="contact__line">
        <svg viewBox="0 0 16 16" aria-hidden="true"><rect x="4" y="1" width="8" height="14" rx="1.5" fill="var(--red)"/><rect x="5.5" y="3" width="5" height="7" fill="#fff"/></svg>
        123-456-0789
      </p>
      <p class="contact__line">
        <svg viewBox="0 0 16 16" aria-hidden="true"><rect x="1" y="3" width="14" height="10" rx="1.5" fill="var(--red)"/><path d="M2 4l6 5 6-5" stroke="#fff" stroke-width="1.4" fill="none"/></svg>
        info@ktplanora.com
      </p>
      <p class="contact__address">Street Name, City Name<br>State Zip Code</p>
    </div>
  </section>

</main>
</body>
</html>
```